New business card with our logo

we finalized our logo with the help of pixel harbor - now we need a business card using that logo. we are a metal service center providing raw steel and metal products for fabricating, contractors, artists, etc. we have the wording for the back of the card figured out (attached, no deviations from text please), just need help putting it all together.
would like the look of steel somehow incorporated in the design ... would like the black part of the logo to be steel or silver color (the S & BRANLEY)
Other font styles liked:
- calibri, arial, similar to those, modern looking
Colors
Designer to choose colors to be used in the design.
Requirements
Must have
- Back of card must haves are attached (no deviations from wording please).
- FRONT of card:
- logo
- address
- name
- office tel
- cell
- fax
- website
- address
Nice to have
- incorporate the look of steel or element of steel somehow
- names of the staff on front not in all caps, i.e. Rosvita not ROSVITA
- this industry is more industrial, not coffee or flower shop so design should be aligned with that
- design should be classic and tasteful

```html
<!DOCTYPE html>
<html lang="en">
<head>
<meta charset="utf-8">
<title>Branley Steel – Business Card</title>
<link rel="stylesheet" href="https://fonts.googleapis.com/css2?family=Arimo:ital,wght@0,700;1,700&display=swap">
<style>
  :root {
    --steel-light: #8d9092;
    --steel-mid: #6b6e70;
    --steel-dark: #45484a;
    --brushed-top: #3a3b3c;
    --brushed-bottom: #141515;
    --ink-dark: #3c3e40;
    --accent-blue: #2a86e8;
    --paper: #eeeeee;
    --white: #ffffff;
  }
  * { margin: 0; padding: 0; box-sizing: border-box; }
  html, body {
    width: 1200px;
    height: 2250px;
    overflow: hidden;
    background: var(--paper);
    font-family: "Arimo", Arial, sans-serif;
  }
  .sheet { position: relative; width: 1200px; height: 2250px; }

  /* Card back: scratched steel */
  .card-back {
    position: absolute; left: 0; top: 0;
    width: 1200px; height: 780px;
    background:
      radial-gradient(ellipse at 45% 40%, var(--steel-light) 0%, var(--steel-mid) 55%, var(--steel-dark) 100%);
  }
  .brand-mark {
    position: absolute; left: 108px; top: 206px;
    width: 204px; height: 204px;
    border-radius: 50%;
    border: 14px solid var(--accent-blue);
  }
  .brand-name {
    position: absolute; left: 340px; top: 242px;
    font-weight: 700; font-size: 84px; line-height: 1;
    letter-spacing: 1px;
    color: var(--accent-blue);
    white-space: nowrap;
  }
  .tagline {
    position: absolute; left: 0; width: 1200px; top: 468px;
    text-align: center;
    font-weight: 700; font-size: 58px; line-height: 1;
    letter-spacing: 2px;
    color: var(--ink-dark);
  }

  /* Card front: brushed dark metal */
  .card-front {
    position: absolute; left: 0; top: 780px;
    width: 1200px; height: 780px;
    background: linear-gradient(180deg, var(--brushed-top) 0%, #262728 50%, var(--brushed-bottom) 100%);
    color: var(--white);
  }
  .front-mark {
    position: absolute; left: 452px; top: 60px;
    width: 300px; height: 300px;
    border-radius: 50%;
    border: 12px solid var(--white);
  }
  .front-name {
    position: absolute; left: 452px; top: 192px; width: 300px;
    text-align: center;
    font-weight: 700; font-size: 30px; line-height: 1;
    color: var(--white);
  }
  .person-name {
    position: absolute; left: 172px; top: 408px;
    font-style: italic; font-weight: 700; font-size: 37px;
  }
  .contact {
    position: absolute; top: 502px;
    list-style: none;
    font-style: italic; font-weight: 700; font-size: 35px; line-height: 53px;
  }
  .contact-left { left: 172px; }
  .contact-right { right: 165px; text-align: right; }
</style>
</head>
<body>
<main class="sheet">
  <section class="card-back" role="img" aria-label="Scratched brushed steel surface with brand name and tagline">
    <div class="brand-mark"></div>
    <div class="brand-name">BRANLEY STEEL</div>
    <div class="tagline">METAL SERVICE CENTER</div>
  </section>

  <section class="card-front" role="img" aria-label="Dark brushed metal card face with contact details">
    <div class="front-mark"></div>
    <div class="front-name">BRANLEY STEEL</div>
    <p class="person-name">John Doe</p>
    <ul class="contact contact-left">
      <li>adress.......</li>
      <li>email@email.com</li>
      <li>www.webadress.com</li>
    </ul>
    <ul class="contact contact-right">
      <li>off: 555-555</li>
      <li>mob: 000-000</li>
      <li>fax: 000-000</li>
    </ul>
  </section>
</main>
</body>
</html>
```